New website for gluVista

We are looking to redesign our e-newsletter gluVista. This a monthly newsletter that publishes the latest research and product news in the diabetes field for people with diabetes. Our current website is here: www.gluvista-news.example.

The parameters are the new site must incorporate our logo, must use the same colors (variation in shade and adding some colors is fine, but the initial pallet should stay) and must be in 1024 by 768 px. It is crucially important that the font in the new design be easily readable (dark, well spaced). If it could be a layered PSD that would be ideal. We have attached 2 sketches of our own brainstorming for a potential lay-out for the home and a new issue page, but these are very rough and should not in any way limit the true designers out there.

We're envisioning a very polished, sophisticated looking magazine-esque site that presents a lot of information. When we were brainstorming for new site ideas we looked at major monthly publications such as the Harbor Ledger (www.harborledger.example) or Velvet Hour (www.vh-mag.example). Like these sites we would still like to feature much of our newest content on the front page, but in a manner that makes good use of space and feels uncluttered. Information needs to be clearly labeled and easy to find. In terms of the overall tone of the website, we do very much want it to be nice and elegant looking site, and one that is targeting a smart, engaged audience.
Updates

Reason: I didn't realize I'd made this due on a Sunday. Please take a couple of extra days everyone.

Industry/Entity Type

News

Requirements
Must have
• The logo. The same color scheme we currently use
Nice to have
• We like the idea of having a featured content box, of using hover buttons on top for our various sections, and potentially using a 3 column setup. However, we are not web designers, so the designer can use these suggestions at their discretion.

```html
<!DOCTYPE html>
<html lang="en">
<head>
<meta charset="utf-8">
<title>gluVista – Research &amp; Product News for people with Diabetes</title>
<link rel="stylesheet" href="https://fonts.googleapis.com/css2?family=Josefin+Sans:wght@400;600&family=Questrial&family=Libre+Baskerville&display=swap">
<style>
:root{
  --teal:#12979b;
  --teal-soft:#6db6ae;
  --teal-pale:#a9d5cf;
  --green:#7dc143;
  --blue:#0d63c4;
  --brown:#4a2a1d;
  --ink:#111;
  --link:#13928f;
  --white:#fff;
}
*{box-sizing:border-box;margin:0;padding:0}
html,body{width:1200px;height:900px;overflow:hidden;background:var(--white)}
.page{position:absolute;left:0;top:0;width:1024px;height:768px;transform:scale(1.171875);transform-origin:0 0;overflow:hidden;background:var(--white);font-family:"Questrial",sans-serif;color:var(--ink)}
.abs{position:absolute}
.nowrap{white-space:nowrap}
.stripe-top{left:0;top:0;width:1024px;height:12px;background:var(--teal)}
.stripe-mid{left:0;top:19px;width:1024px;height:6px;background:var(--teal)}
.header{left:0;top:27px;width:1024px;height:128px;background:radial-gradient(circle at 640px 50px,#3fb3b2 0,var(--teal) 140px),var(--teal)}
.header-fade{left:0;top:27px;width:414px;height:16px;background:linear-gradient(90deg,#14999d,#4bb0ae)}
.accent-blue{left:418px;top:27px;width:16px;height:16px;background:var(--blue)}
.accent-green{left:437px;top:27px;width:587px;height:16px;background:var(--green)}
.brand{left:6px;top:45px;font-family:"Libre Baskerville",serif;font-size:88px;line-height:1;color:var(--brown);letter-spacing:-2px}
.tagline{left:405px;top:76px;width:300px;font-size:17px;line-height:26px;color:var(--white);text-align:right;white-space:nowrap}
.tagline span{display:block}
.print{left:774px;top:80px;font-family:"Josefin Sans",sans-serif;font-size:12px;letter-spacing:3px;line-height:19px;color:#111;text-transform:uppercase;white-space:nowrap}
.pdf{left:962px;top:73px;width:39px;height:52px;background:#f4f4f4;border:1px solid #c9c9c9}
.pdf::after{content:"";position:absolute;left:6px;top:6px;width:24px;height:10px;background:#d5261e}
.nav{left:0;top:155px;width:1024px;height:57px;background:var(--teal-soft)}
.nav-rule{left:12px;top:169px;width:990px;height:1px;background:#3b8f88}
.nav-list{left:68px;top:182px;display:flex;list-style:none}
.nav-list li{border-left:3px solid #dfeeec;padding:6px 0 0 14px;height:30px;font-family:"Josefin Sans",sans-serif;font-variant:small-caps;font-size:17px;letter-spacing:2.5px;color:var(--white);white-space:nowrap}
.nav-list li:nth-child(1){width:112px}
.nav-list li:nth-child(2){width:124px}
.nav-list li:nth-child(3){width:130px}
.nav-list li:nth-child(4){width:127px}
.search-label{left:768px;top:188px;font-family:"Josefin Sans",sans-serif;font-variant:small-caps;font-size:17px;letter-spacing:2.5px;color:var(--white)}
.search-box{left:851px;top:181px;width:139px;height:26px;background:#f4fbfb}
.stage{left:0;top:212px;width:1024px;height:310px;background:linear-gradient(180deg,#666 0,#aaa 55px,#e5e5e5 150px,#fff 300px)}
.issue-panel{left:12px;top:225px;width:243px;height:270px;background:linear-gradient(180deg,rgba(200,200,200,.85),rgba(245,245,245,.9) 90px,#f6f6f6)}
.issue-mark{left:18px;top:244px;font-family:"Libre Baskerville",serif;font-size:42px;line-height:1;color:#a8e6f2}
.issue-date{left:82px;top:244px;font-family:"Josefin Sans",sans-serif;font-size:15px;letter-spacing:2.5px;line-height:20px;color:var(--white);white-space:nowrap}
.issue-rule{left:12px;top:309px;width:243px;height:1px;background:#777}
.contents{left:31px;top:320px;list-style:none;font-size:12.5px;line-height:21px;color:var(--link);white-space:nowrap}
.contents li::before{content:"• "}
.featured{left:270px;top:225px;width:742px;height:270px;background:rgba(243,243,243,.95)}
.featured-title{left:287px;top:243px;font-family:"Josefin Sans",sans-serif;font-variant:small-caps;font-weight:400;font-size:17px;letter-spacing:2px;color:#111;white-space:nowrap}
.body-text{font-size:10.5px;line-height:18.5px;white-space:nowrap}
.featured-intro{left:478px;top:244px}
.featured-rule{left:270px;top:309px;width:728px;height:1px;background:#222}
.photo-lead{left:278px;top:316px;width:422px;height:173px;background:linear-gradient(90deg,#2a2a2a,#8a8580 40%,#c9c3ba 70%,#e2ddd6)}
.photo-lab{left:709px;top:316px;width:113px;height:95px;background:linear-gradient(135deg,#c8ccd0,#7c8288 60%,#3e4348)}
.featured-side{left:832px;top:313px}
.featured-body{left:711px;top:419px}
.grid-rule{left:18px;top:512px;width:980px;height:1px;background:#222}
.card-head{font-size:12.5px;color:var(--link);white-space:nowrap}
.card-head::before{content:"• "}
.footer{left:0;top:724px;width:1024px;height:44px;background:var(--teal-pale)}
.footer-brand{left:14px;top:729px;font-family:"Libre Baskerville",serif;font-size:28px;line-height:1;color:#4c8e8a}
.copyright{left:287px;top:744px;font-family:"Josefin Sans",sans-serif;font-size:9px;letter-spacing:1.5px;color:#333;white-space:nowrap}
.footer-links{left:492px;top:740px;font-family:"Josefin Sans",sans-serif;font-variant:small-caps;font-size:15px;letter-spacing:2px;color:#333;white-space:nowrap}
.social{top:733px;width:27px;height:27px}
.feed{left:899px;background:#e2771f}
.chirp{left:941px;background:#3da9e0}
.friend{left:984px;background:#3a5da8}
</style>
</head>
<body>
<div class="page">
  <div class="abs stripe-top"></div>
  <div class="abs stripe-mid"></div>
  <header>
    <div class="abs header"></div>
    <div class="abs header-fade"></div>
    <div class="abs accent-blue"></div>
    <div class="abs accent-green"></div>
    <div class="abs brand">gluVista</div>
    <p class="abs tagline"><span>Research &amp; Product News for people</span><span>with Diabetes.</span></p>
    <p class="abs print">Print our latest<br>issue here.</p>
    <div class="abs pdf" role="img" aria-label="Download PDF"></div>
  </header>
  <nav>
    <div class="abs nav"></div>
    <div class="abs nav-rule"></div>
    <ul class="abs nav-list"><li>Home</li><li>Issues</li><li>Columns</li><li>Topics</li><li>About Us</li></ul>
    <div class="abs search-label">Search</div>
    <div class="abs search-box"></div>
  </nav>
  <main>
    <div class="abs stage"></div>
    <aside>
      <div class="abs issue-panel"></div>
      <div class="abs issue-mark">gV</div>
      <p class="abs issue-date">JANUARY, 2011<br>ISSUE #28</p>
      <div class="abs issue-rule"></div>
      <ul class="abs contents">
        <li>From the Editor</li><li>New now next</li><li>Sum musings</li><li>Quotable quotes</li><li>Learning Curve</li><li>Thinking like a pancreas</li><li>Trial Watch</li><li>Finger sticks</li>
      </ul>
    </aside>
    <section>
      <div class="abs featured"></div>
      <h2 class="abs featured-title">Featured Content</h2>
      <p class="abs body-text featured-intro">New inventions and research are on the<br>horizon. New treatments give patients more<br>choices and freedom.</p>
      <div class="abs featured-rule"></div>
      <div class="abs photo-lead" role="img" aria-label="Researcher examining a test tube in a laboratory"></div>
      <div class="abs photo-lab" role="img" aria-label="Scientists working in a bright laboratory"></div>
      <p class="abs body-text featured-side">New inventions and research are<br>on the horizon. New treatments<br>give patients more choices and<br>freedom.</p>
      <p class="abs body-text featured-body">New inventions and research are on the horizon. New<br>treatments give patients more choices and freedom.<br>New inventions and research are on the horizon. New<br>treatments give patients more choices and freedom.</p>
    </section>
    <div class="abs grid-rule"></div>
    <section>
      <p class="abs card-head" style="left:19px;top:526px">From the Editor</p>
      <div class="abs" style="left:19px;top:549px;width:86px;height:76px;background:linear-gradient(135deg,#8a6a52,#d8b7a0 50%,#5d5a57)" role="img" aria-label="Portrait of the editor"></div>
      <p class="abs body-text" style="left:117px;top:546px">Join in with people around<br>the world&nbsp; Planet earth<br>is blue and there's<br>something we can do.</p>

      <p class="abs card-head" style="left:269px;top:526px">From the Editor</p>
      <div class="abs" style="left:271px;top:549px;width:90px;height:76px;background:linear-gradient(90deg,#6f6f6f,#c9c9c9 50%,#7a7a7a)" role="img" aria-label="Medicine bottles"></div>
      <p class="abs body-text" style="left:369px;top:546px">Join in with people around<br>the world&nbsp; Planet earth<br>is blue and there's<br>something we can do.</p>

      <p class="abs card-head" style="left:519px;top:526px">From the Editor</p>
      <div class="abs" style="left:526px;top:549px;width:50px;height:72px;background:radial-gradient(circle,#e9b64a,#c5432b 60%,#fff 72%)" role="img" aria-label="Illustration of a kidney"></div>
      <p class="abs body-text" style="left:611px;top:546px">Join in with people around<br>the world&nbsp; Planet earth<br>is blue and there's<br>something we can do.</p>

      <p class="abs card-head" style="left:768px;top:526px">From the Editor</p>
      <div class="abs" style="left:770px;top:551px;width:90px;height:74px;background:linear-gradient(135deg,#3d6fb0,#c8ccd0 50%,#e7a6b3)" role="img" aria-label="Glucose meters in several colours"></div>
      <p class="abs body-text" style="left:868px;top:546px">Join in with people around<br>the world&nbsp; Planet earth<br>is blue and there's<br>something we can do.</p>

      <p class="abs card-head" style="left:19px;top:636px">New, now, next</p>
      <div class="abs" style="left:19px;top:657px;width:88px;height:61px;background:linear-gradient(135deg,#e8e8e8,#a9aba6 60%,#d7d7d2)" role="img" aria-label="Insulin pump device"></div>
      <p class="abs body-text" style="left:117px;top:655px">Join in with people around<br>the world&nbsp; Planet earth is<br>blue and there's something.</p>

      <p class="abs card-head" style="left:277px;top:632px">From the Editor</p>
      <div class="abs" style="left:269px;top:655px;width:92px;height:56px;background:linear-gradient(90deg,#d9d4cf,#b8b1aa 50%,#efebe6)" role="img" aria-label="Researcher in a laboratory"></div>
      <p class="abs body-text" style="left:369px;top:655px">Join in with people around<br>the world&nbsp; Planet earth is<br>blue and there's something.</p>

      <p class="abs card-head" style="left:521px;top:632px">From the Editor</p>
      <div class="abs" style="left:525px;top:655px;width:79px;height:59px;background:linear-gradient(180deg,#2c5fa8,#6f9bd0 50%,#e6edf3)" role="img" aria-label="Mountaineer in cold weather gear"></div>
      <p class="abs body-text" style="left:611px;top:655px">Join in with people around<br>the world&nbsp; Planet earth is<br>blue and there's something.</p>

      <p class="abs card-head" style="left:768px;top:632px">From the Editor</p>
      <div class="abs" style="left:782px;top:655px;width:60px;height:60px;background:radial-gradient(circle,#3f9aa3,#d97a86 55%,#fff 75%)" role="img" aria-label="Molecular illustration of a cell receptor"></div>
      <p class="abs body-text" style="left:868px;top:655px">Join in with people around<br>the world&nbsp; Planet earth is<br>blue and there's something.</p>
    </section>
  </main>
  <footer>
    <div class="abs footer"></div>
    <div class="abs footer-brand">gluVista</div>
    <p class="abs copyright">2011 GLUVISTA</p>
    <p class="abs footer-links">Contact us &nbsp;•&nbsp; Archives &nbsp;•&nbsp; A &nbsp;A &nbsp;a</p>
    <div class="abs social feed" role="img" aria-label="News feed"></div>
    <div class="abs social chirp" role="img" aria-label="Chirpline"></div>
    <div class="abs social friend" role="img" aria-label="Friendhub"></div>
  </footer>
</div>
</body>
</html>
```